Falcrest security business card

Looking for a business card for my security company

Target Market(s)

Security

Industry/Entity Type

Security

Contact Information for Business Card

Name - Gil Marston. Title - General manager - direct 314 862.4490 website www. falcrestsecurityservices.example email - gil@ falcrestsecurityservices.example

Requirements
Must have
• Logo attached

```html
<!DOCTYPE html>
<html lang="en">
<head>
<meta charset="utf-8">
<title>Falcrest Security Services – Business Cards</title>
<link rel="stylesheet" href="https://fonts.googleapis.com/css2?family=Oswald:wght@400;500;700&display=swap">
<style>
  :root {
    --backdrop: #c9cbcd;
    --ink-black: #141414;
    --ink-black-soft: #2b2b2b;
    --gold-deep: #b08238;
    --gold-mid: #cfa45a;
    --gold-light: #e3c783;
    --text-dark: #1a1a1a;
  }
  * { box-sizing: border-box; margin: 0; padding: 0; }
  html, body { width: 1200px; height: 800px; overflow: hidden; }
  body {
    background: var(--backdrop);
    font-family: "Oswald", sans-serif;
    position: relative;
  }
  .card {
    position: absolute;
    width: 520px;
    height: 297px;
    border-radius: 4px;
    overflow: hidden;
    box-shadow: 0 10px 24px rgba(0,0,0,0.28);
    display: flex;
    flex-direction: column;
  }
  .card--logo-black { left: 60px; top: 83px; background: linear-gradient(160deg, var(--ink-black), var(--ink-black-soft)); }
  .card--logo-split { left: 620px; top: 83px; }
  .card--contact    { left: 340px; top: 420px; }

  .band-black {
    background: linear-gradient(160deg, var(--ink-black), var(--ink-black-soft));
    display: flex; align-items: center; justify-content: center;
  }
  .band-gold {
    flex: 1;
    background: linear-gradient(120deg, var(--gold-deep), var(--gold-mid) 55%, var(--gold-light));
    display: flex; flex-direction: column; align-items: center; justify-content: center;
    color: var(--text-dark);
    text-align: center;
  }

  .brand {
    display: flex; align-items: center; gap: 12px;
    color: var(--gold-mid);
  }
  .brand__dot {
    width: 16px; height: 16px; border-radius: 50%;
    background: var(--gold-mid);
  }
  .brand__name {
    font-weight: 700;
    font-size: 58px;
    letter-spacing: 3px;
    text-transform: uppercase;
    line-height: 1;
  }
  .brand--small .brand__name { font-size: 46px; }

  .card--logo-black .brand { margin-top: 92px; justify-content: center; }
  .card--logo-black .website {
    margin-top: 46px; text-align: center;
    color: var(--gold-mid); font-weight: 500; font-size: 19px; letter-spacing: 0.5px;
  }

  .card--logo-split .band-black { height: 150px; }
  .card--logo-split .website { font-weight: 500; font-size: 21px; letter-spacing: 0.5px; }

  .card--contact .band-black { height: 110px; }
  .contact__name { font-weight: 700; font-size: 28px; letter-spacing: 1px; text-transform: uppercase; line-height: 1.1; }
  .contact__title { font-weight: 400; font-size: 17px; margin-bottom: 10px; }
  .contact__line { font-weight: 400; font-size: 16px; line-height: 1.35; }
  .contact__email { font-weight: 500; }
</style>
</head>
<body>
  <section class="card card--logo-black">
    <div class="brand">
      <span class="brand__dot"></span>
      <span class="brand__name">Falcrest</span>
    </div>
    <p class="website">www. falcrestsecurityservices.example</p>
  </section>

  <section class="card card--logo-split">
    <div class="band-black">
      <div class="brand">
        <span class="brand__dot"></span>
        <span class="brand__name">Falcrest</span>
      </div>
    </div>
    <div class="band-gold">
      <p class="website">www. falcrestsecurityservices.example</p>
    </div>
  </section>

  <section class="card card--contact">
    <div class="band-black">
      <div class="brand brand--small">
        <span class="brand__dot"></span>
        <span class="brand__name">Falcrest</span>
      </div>
    </div>
    <div class="band-gold">
      <p class="contact__name">Gil Marston</p>
      <p class="contact__title">General Manager</p>
      <p class="contact__line">314 862.4490</p>
      <p class="contact__line">falcrestsecurityservices.example</p>
      <p class="contact__line contact__email">gil@ falcrestsecurityservices.example</p>
    </div>
  </section>
</body>
</html>
```